Revamp Landing Page

Our current landing page is http://velvetdenkx.com/ and we're looking for our site to look like this http://www.goldparrotclub.com/. Classy, Sleek, Simple elegant.

The site should be desktop and mobile optimized.
Pages should be built out and the same structure. Drink Menu, Gallery, Events, Table Reservations, Membership, Press, Contact Us.

Feel free to use the images on our website.

```html
<!DOCTYPE html>
<html lang="en">
<head>
<meta charset="utf-8">
<title>Velvet Den — Landing Page</title>
<link href="https://fonts.googleapis.com/css2?family=Tinos&family=Lora:ital@1&display=swap" rel="stylesheet">
<style>
  :root {
    --stage: #0e0e0e;
    --paper: #ffffff;
    --ink: #1a1a1a;
    --band: #000000;
    --band-text: #f2f2f2;
    --photo-deep: #1c0f08;
    --photo-warm: #b9803e;
    --photo-glow: #f1d8a0;
  }
  * { box-sizing: border-box; margin: 0; padding: 0; }
  html, body { width: 1200px; height: 773px; overflow: hidden; }
  body { background: var(--stage); position: relative; font-family: "Tinos", serif; color: var(--ink); }

  .screen { position: absolute; background: var(--paper); box-shadow: 0 4px 10px rgba(0,0,0,.5); }
  .screen--desktop { left: 54px; top: 87px; width: 732px; height: 589px; }
  .screen--mobile { left: 815px; top: 87px; width: 330px; height: 589px; }

  .brand { font-family: "Tinos", serif; font-weight: 400; color: var(--ink); letter-spacing: 2px; white-space: nowrap; }

  .bar-photo {
    position: absolute;
    background:
      radial-gradient(ellipse 45% 35% at 50% 38%, var(--photo-glow) 0%, var(--photo-warm) 45%, transparent 80%),
      linear-gradient(180deg, var(--photo-deep) 0%, #5a3319 55%, var(--photo-deep) 100%);
  }

  /* desktop */
  .desktop-brand { position: absolute; top: 38px; left: 0; width: 100%; text-align: center; font-size: 30px; line-height: 38px; }
  .main-nav { position: absolute; top: 109px; left: 0; width: 100%; display: flex; justify-content: center; gap: 13px; list-style: none; font-size: 9px; line-height: 12px; letter-spacing: .1px; white-space: nowrap; }
  .desktop-photo { left: 146px; top: 159px; width: 441px; height: 293px; }
  .desktop-intro { position: absolute; top: 473px; left: 0; width: 100%; text-align: center; }
  .desktop-intro h1 { font-weight: 400; font-size: 12px; line-height: 15px; letter-spacing: .2px; }
  .desktop-intro p { font-family: "Lora", serif; font-style: italic; font-size: 9px; line-height: 12px; margin-top: 10px; }
  .desktop-footer { position: absolute; left: 0; bottom: 0; width: 100%; height: 34px; background: var(--band); color: var(--band-text); display: flex; align-items: center; justify-content: center; gap: 14px; font-size: 7.5px; }

  .social { display: flex; gap: 10px; list-style: none; }
  .social li { width: 10px; height: 10px; border-radius: 50%; background: var(--band-text); }

  /* mobile */
  .mobile-header { position: absolute; top: 0; left: 0; width: 100%; height: 102px; }
  .mobile-brand { position: absolute; left: 34px; top: 34px; font-size: 25px; line-height: 30px; }
  .menu-toggle { position: absolute; right: 38px; top: 38px; }
  .mobile-photo { left: 0; top: 102px; width: 330px; height: 220px; }
  .mobile-intro { position: absolute; top: 359px; left: 0; width: 100%; text-align: center; }
  .mobile-intro h1 { font-weight: 400; font-size: 16px; line-height: 19px; }
  .mobile-intro p { font-family: "Lora", serif; font-style: italic; font-size: 12px; line-height: 15px; margin-top: 16px; }
  .mobile-footer { position: absolute; left: 0; bottom: 0; width: 100%; height: 90px; background: var(--band); color: var(--band-text); text-align: center; font-size: 9.5px; line-height: 13px; padding-top: 20px; }
  .mobile-footer .social { justify-content: center; margin-top: 14px; gap: 16px; }
  .mobile-footer .social li { width: 14px; height: 14px; }
</style>
</head>
<body>

<section class="screen screen--desktop">
  <div class="brand desktop-brand">VELVET DEN</div>
  <ul class="main-nav">
    <li>DRINK MENU</li><li>GALLERY</li><li>EVENTS</li><li>TABLE RESERVATIONS</li><li>MEMBERSHIP</li><li>PRESS</li><li>CONTACT US</li>
  </ul>
  <div class="bar-photo desktop-photo" role="img" aria-label="Photo of the candlelit bar with backlit bottle shelves, wooden stools and lounge seating"></div>
  <div class="desktop-intro">
    <h1>VELVET DEN: A HOME AWAY FROM HOME FOR THE LOCAL COMMUNITY.</h1>
    <p>At Velvet Den, it is our goal to make sure that you enjoy every moment in your experience.<br>Consider us your liaisons to happiness...</p>
  </div>
  <footer class="desktop-footer">
    <span>57 LANTERN WHARF RD PORT AVERLY, CALIFORNIA 90877 INFO@VELVETDENKX.COM</span>
    <ul class="social" aria-label="Social links"><li></li><li></li><li></li></ul>
  </footer>
</section>

<section class="screen screen--mobile">
  <header class="mobile-header">
    <div class="brand mobile-brand">VELVET DEN</div>
    <svg class="menu-toggle" width="28" height="20" viewBox="0 0 28 20" aria-label="Menu">
      <rect x="0" y="0" width="28" height="3" fill="#000"/>
      <rect x="0" y="8.5" width="28" height="3" fill="#000"/>
      <rect x="0" y="17" width="28" height="3" fill="#000"/>
    </svg>
  </header>
  <div class="bar-photo mobile-photo" role="img" aria-label="Photo of the candlelit bar with backlit bottle shelves, wooden stools and lounge seating"></div>
  <div class="mobile-intro">
    <h1>VELVET DEN: A HOME AWAY FROM<br>HOME FOR THE LOCAL COMMUNITY.</h1>
    <p>At Velvet Den, it is our goal to make sure<br>that you enjoy every moment in your experience.<br>Consider us your liaisons to happiness...</p>
  </div>
  <footer class="mobile-footer">
    <div>57 LANTERN WHARF RD PORT AVERLY,<br>CALIFORNIA 90877 INFO@VELVETDENKX.COM</div>
    <ul class="social" aria-label="Social links"><li></li><li></li><li></li></ul>
  </footer>
</section>

</body>
</html>
```